THE HOMESTEAD LEDGER
STATIONARY, ENVELOPES, FLYERS, BUSINESS CARDS
Project: THE HOMESTEAD LEDGER
THE HOMESTEAD LEDGER - Real Estate
Creative Brief
Professional
MALCOLM J. VANTREASE
PRINCIPAL BROKER
518 WILLOWCREST DRIVE BRAMBLEFORD, OREGON 97999
malcolmvantrease@quillmail.example
FRONT SIDE DESIGN AND/OR LOGO WITH INDIVIDUAL INFORMATION AND AREA FOR INDIVIDUAL PICTURE.
AT LEAST "THE HOMESTEAD LEDGER" LOGO. OPEN TO OTHER DESIGN AND/OR BORDERS WITH IT.

```html
<!DOCTYPE html>
<html lang="en">
<head>
<meta charset="utf-8">
<title>The Homestead Ledger – Stationery Set</title>
<link href="https://fonts.googleapis.com/css2?family=Cinzel:wght@600&family=Lato:wght@400;700&display=swap" rel="stylesheet">
<style>
  :root {
    --backdrop: #4e3a2c;
    --paper: #ffffff;
    --olive: #8c875a;
    --olive-dark: #6f6b44;
    --olive-light: #b4b088;
    --ink: #4a4a44;
    --brand: #5c5c56;
    --faint: #ecece8;
    --band-text: #f4f2e6;
  }
  * { box-sizing: border-box; margin: 0; padding: 0; }
  html, body { width: 1200px; height: 732px; overflow: hidden; }
  body { background: var(--backdrop); position: relative; font-family: "Lato", sans-serif; }

  .brand-name {
    font-family: "Cinzel", serif; font-weight: 600; color: var(--brand);
    line-height: 1.05; letter-spacing: 0.04em; text-transform: uppercase;
  }

  /* Letterhead */
  .letterhead { position: absolute; left: 115px; top: 29px; width: 480px; height: 672px;
    background: var(--paper); box-shadow: 0 3px 10px rgba(0,0,0,.45); }
  .letterhead .brand-name { position: absolute; left: 32px; top: 40px; font-size: 16px; width: 150px; }
  .letterhead .watermark { position: absolute; left: 0; right: 0; top: 300px; width: auto;
    text-align: center; font-size: 34px; line-height: 1.15; color: var(--faint); white-space: nowrap; }
  .footer-band { position: absolute; left: 0; right: 0; bottom: 0; height: 24px; background: var(--olive);
    display: flex; justify-content: space-between; align-items: center; padding: 0 14px;
    font-size: 7px; letter-spacing: .06em; color: var(--band-text); white-space: nowrap; }

  /* Business cards */
  .card { position: absolute; top: 72px; width: 166px; height: 96px; border-radius: 6px; overflow: hidden;
    box-shadow: 0 2px 6px rgba(0,0,0,.45); }
  .card-front { left: 672px; background: linear-gradient(180deg, var(--olive-light), var(--olive)); }
  .card-front .brand-name { position: absolute; left: 0; right: 0; top: 34px; text-align: center;
    font-size: 11px; color: var(--paper); }
  .card-back { left: 845px; background: var(--paper); }
  .card-back .olive-side { position: absolute; inset: 0; }
  .card-back .brand-name { position: absolute; left: 6px; top: 38px; width: 74px; text-align: center;
    font-size: 7.5px; color: var(--paper); }
  .card-back .details { position: absolute; left: 94px; top: 10px; width: 68px; text-align: center;
    font-size: 4.5px; color: var(--ink); line-height: 1.4; }
  .card-back .details .agent { font-weight: 700; font-size: 5px; }
  .portrait { display: block; width: 26px; height: 34px; margin: 6px auto; background: linear-gradient(#e2e0d4, #c9c6b2);
    border: 1px solid var(--olive); }

  /* Envelope front */
  .envelope-front { position: absolute; left: 605px; top: 197px; width: 480px; height: 216px;
    background: var(--paper); box-shadow: 0 3px 8px rgba(0,0,0,.45); }
  .envelope-front .brand-name { position: absolute; left: 36px; top: 28px; font-size: 14px; width: 140px; }
  .envelope-front .return-band { position: absolute; left: 0; right: 0; bottom: 0; height: 30px;
    background: var(--olive); font-size: 7px; letter-spacing: .06em; color: var(--band-text);
    text-align: center; padding-top: 5px; }

  /* Envelope back */
  .envelope-back { position: absolute; left: 605px; top: 427px; width: 480px; height: 226px;
    background: var(--paper); box-shadow: 0 3px 8px rgba(0,0,0,.45); }
  .envelope-back svg { position: absolute; inset: 0; }
  .envelope-back .brand-name { position: absolute; left: 0; right: 0; top: 44px; text-align: center;
    font-size: 15px; color: rgba(255,255,255,.4); }
</style>
</head>
<body>

<section class="letterhead">
  <div class="brand-name">The Homestead Ledger</div>
  <div class="brand-name watermark">The Homestead<br>Ledger</div>
  <div class="footer-band">
    <span>518 WILLOWCREST DRIVE BRAMBLEFORD, OREGON 97999</span>
    <span>(270) 555-0148</span>
    <span>malcolmvantrease@quillmail.example</span>
  </div>
</section>

<section class="card card-front">
  <div class="brand-name">The Homestead Ledger</div>
</section>

<section class="card card-back">
  <svg class="olive-side" width="166" height="96" viewBox="0 0 166 96">
    <defs>
      <linearGradient id="cardOlive" x1="0" y1="0" x2="0" y2="1">
        <stop offset="0" stop-color="#b4b088"/><stop offset="1" stop-color="#8c875a"/>
      </linearGradient>
    </defs>
    <path d="M0 0 H86 Q96 48 86 96 H0 Z" fill="url(#cardOlive)"/>
  </svg>
  <div class="brand-name">The Homestead Ledger</div>
  <div class="details">
    <div class="agent">MALCOLM J. VANTREASE</div>
    <div>PRINCIPAL BROKER</div>
    <div class="portrait" role="img" aria-label="Space for the broker's portrait photo"></div>
    <div>518 WILLOWCREST DRIVE</div>
    <div>(270) 555-0148</div>
  </div>
</section>

<section class="envelope-front">
  <div class="brand-name">The Homestead Ledger</div>
  <div class="return-band">518 WILLOWCREST DRIVE BRAMBLEFORD, OREGON 97999</div>
</section>

<section class="envelope-back">
  <svg width="480" height="226" viewBox="0 0 480 226">
    <defs>
      <linearGradient id="flapOlive" x1="0" y1="0" x2="0" y2="1">
        <stop offset="0" stop-color="#8c875a"/><stop offset="1" stop-color="#b4b088"/>
      </linearGradient>
    </defs>
    <path d="M0 0 H480 V14 Q462 18 448 50 Q432 96 390 98 H90 Q48 96 32 50 Q18 18 0 14 Z" fill="url(#flapOlive)"/>
    <path d="M0 0 H480 V6 H0 Z" fill="#6f6b44"/>
  </svg>
  <div class="brand-name">The Homestead Ledger</div>
</section>

</body>
</html>
```